Process Diagram - Circular Economy

I would like for a designer to take this rough sketch and turn it into a high quality design which can be used in a business presentation. Seeking to get both PDF and Jpeg file versions of the finished product.

Colours don't have to be the exact same as the rough sketch PDF, the green used is pretty ugly so open to some changes.

Target Market(s)

Corporate audience

Requirements
Must have
• Clear text for each party; VENOR, KORMIT, BUYER

Smaller text for the functions; marketing, recovery, logistics, cleaning, decontamination, testing & re-certification, storage, engineering suitability

```html
<!DOCTYPE html>
<html lang="en">
<head>
<meta charset="utf-8">
<title>Circular Economy Process</title>
<link rel="stylesheet" href="https://fonts.googleapis.com/css2?family=Fira+Sans:wght@400;700;800&display=swap">
<style>
  :root {
    --bg: #ffffff;
    --navy: #1d4a6a;
    --leaf: #8cc63f;
    --blue-light: #5eaadf;
    --blue-deep: #1470bb;
    --orange: #c97a2b;
    --green-dark: #739e4f;
    --green-mid: #86ad58;
    --green-light: #b2d86c;
    --ink-light: #ffffff;
  }
  html, body {
    margin: 0;
    padding: 0;
    width: 1200px;
    height: 1200px;
    overflow: hidden;
    background: var(--bg);
  }
  .diagram {
    display: block;
    width: 1200px;
    height: 1200px;
    font-family: "Fira Sans", sans-serif;
  }
  .label-stage { fill: var(--ink-light); font-size: 24px; font-weight: 400; }
  .label-party { fill: var(--ink-light); font-size: 52px; font-weight: 800; }
  .label-hub { fill: var(--ink-light); font-size: 40px; font-weight: 700; }
  .label-phase { font-size: 40px; font-weight: 800; }
  .label-phase--end { fill: var(--navy); }
  .label-phase--new { fill: var(--leaf); }
</style>
</head>
<body>
<svg class="diagram" viewBox="0 0 1920 1920" xmlns="http://www.w3.org/2000/svg" aria-label="Circular economy process from vendor through Kormit to buyer">
  <defs>
    <linearGradient id="ring-fill" x1="760" y1="980" x2="1010" y2="1220" gradientUnits="userSpaceOnUse">
      <stop offset="0" stop-color="var(--green-dark)"/>
      <stop offset="1" stop-color="var(--orange)"/>
    </linearGradient>
    <linearGradient id="ring-top" x1="1080" y1="840" x2="1180" y2="1000" gradientUnits="userSpaceOnUse">
      <stop offset="0" stop-color="var(--blue-deep)"/>
      <stop offset="1" stop-color="var(--orange)" stop-opacity="0"/>
    </linearGradient>
    <linearGradient id="vendor-fill" x1="370" y1="0" x2="1200" y2="0" gradientUnits="userSpaceOnUse">
      <stop offset="0" stop-color="var(--blue-light)"/>
      <stop offset="0.6" stop-color="var(--blue-deep)"/>
      <stop offset="1" stop-color="var(--blue-deep)"/>
    </linearGradient>
    <linearGradient id="buyer-fill" x1="1100" y1="0" x2="1560" y2="0" gradientUnits="userSpaceOnUse">
      <stop offset="0" stop-color="var(--green-mid)"/>
      <stop offset="1" stop-color="var(--green-light)"/>
    </linearGradient>
    <linearGradient id="suitability-fill" x1="640" y1="0" x2="1220" y2="0" gradientUnits="userSpaceOnUse">
      <stop offset="0" stop-color="var(--green-light)"/>
      <stop offset="1" stop-color="var(--green-mid)"/>
    </linearGradient>
  </defs>

  <g class="hub-ring">
    <path fill="url(#ring-fill)" fill-rule="evenodd"
      d="M963,758 a270,270 0 1,0 0.1,0 Z M963,898 a130,130 0 1,1 -0.1,0 Z"/>
    <path fill="url(#ring-top)" d="M1100,820 C1170,870 1220,940 1232,1028 L1093,1028 C1093,960 1050,910 1000,900 Z"/>
  </g>

  <path class="band-suitability" fill="url(#suitability-fill)"
    d="M640,688 C760,708 870,718 970,720 C1080,722 1160,790 1220,878 L1190,882 C1130,800 1060,760 970,758 C850,752 740,740 640,725 Z"/>

  <path class="band-buyer" fill="url(#buyer-fill)"
    d="M1095,750 C1250,735 1350,715 1455,690 L1562,722 L1488,820 C1400,850 1300,865 1218,878 C1180,820 1140,780 1095,750 Z"/>

  <path class="band-vendor" fill="url(#vendor-fill)"
    d="M370,652 C520,715 760,752 970,758 C1080,762 1160,830 1195,880 L1130,950 C1100,905 1040,878 970,876 C800,868 620,840 497,800 L497,835 C450,822 410,808 370,793 Z"/>

  <path class="band-marketing" fill="var(--orange)"
    d="M510,816 C640,850 800,870 970,876 C1060,878 1120,930 1135,1000 L1135,1028 L1093,1028 C1093,960 1040,914 970,914 C820,912 650,885 510,852 Z"/>

  <text class="label-phase label-phase--end" transform="translate(432,668) rotate(13)">End of Life</text>
  <text class="label-party" transform="translate(428,764) rotate(10)">VENDOR</text>
  <text class="label-stage" transform="translate(654,722) rotate(5)">Engineering Suitability</text>
  <text class="label-stage" x="915" y="832">Recovery</text>
  <text class="label-stage" transform="translate(564,856) rotate(10)">Marketing</text>

  <text class="label-phase label-phase--new" transform="translate(1240,720) rotate(-10)">New Life</text>
  <text class="label-party" transform="translate(1266,818) rotate(-10)">BUYER</text>

  <text class="label-stage" x="1112" y="974">Logistics</text>
  <text class="label-stage" x="1125" y="1041">Storage</text>
  <text class="label-stage" x="1106" y="1108">Cleaning</text>
  <text class="label-hub" x="1032" y="1186">KORMIT</text>
  <text class="label-stage" x="757" y="1152">Testing &amp;</text>
  <text class="label-stage" x="757" y="1182">Re-certification</text>
  <text class="label-stage" x="867" y="1248">Decontamination</text>
</svg>
</body>
</html>
```